詳細はzipファイルにまとめておりおますので、こちらからダウンロードしてください。

http://3.hakobuya.nu/0522-k83920fa17de462093b8e1c7f06a35d9

【デザインの参考サイト】
クライアント様からは、以下の参考サイトを挙げていただいております。
http://plumtivra.com/
https://sorvik4417.com/

ただし、上記サイトはおしゃれではあるものの、少しアピールが弱いようにも思います。
最終的な成果(査定依頼や、来店予約)に結びつきやすいような工夫があれば嬉しいです。

【継続発注について】
まずはトップページのみのデザインをお願い致します。
トップページのデザインが決まりましたら、下層ページのデザインもお願いする予定です。(1ページ1~2万円程度の予定)
下層ページは2~3ページほどの予定ですので、総額12万円ぐらいの予定です。

【スマホ対応について】
コーディング時に、レスポンシブ対応する予定ですので、スマホ対応しやすいデザインにしていただければ助かります。

【レイアウトの変更などについて】
基本的にはワイヤーに沿って作っていただければと思います。
ただし、「もっとこうしたほうが良いのでは?」「こんな形はどうか?」といったようなご提案があれば、別途ご相談ください。

必要な資料は上記のzipファイルの中に入れておりますので、そちらをご覧ください。
もし不明な点があれば遠慮なくご連絡くださいませ。
1ページ
シンプル 複雑
単色 カラフル
暗い 明るい
日常 高級
遊び心 厳粛
未来的 伝統的
女性的 男性的
黄・オレンジ系
• 高解像度JPG (.jpg)
• イラストレーター形式 (.ai)
納品は、IllustratorでもPhotoshopでもFireworksでも、どのファイルでもOKです。

また、納品の際には使っているフォントをお教えください。
(使用フォントはモリサワ、もしくはフリーフォントでお願いします)
たくさんのご応募ありがとうございました。
非常に悩んだのですが、お一人の方を選ばせていただきました。
選に漏れた方々につきましては、お手数おかけしたにも関わらず何もお返しできずに心苦しくもあるのですが、ご了承いただければ幸いです。
またこれに懲りず、今後ともよろしくお願いいたします。
ありがとうございました!

いいデザインをしていただいた方が数人おられて、非常に悩みました。
その中で一番こちらの意図を汲み取っていただき、バランスの取れたデザインをしていただいた、ということで、こちらの方にお願いすることにしました。

たくさんのご応募ありがとうございました。
ありがとうございました!

```html
<!DOCTYPE html>
<html lang="ja">
<head>
<meta charset="UTF-8">
<title>タカミエ | 7階以上の高層階マンション売買サービス</title>
<link href="https://fonts.googleapis.com/css2?family=Noto+Sans+JP:wght@400;500;700&display=swap" rel="stylesheet">
<style>
:root{
  --orange:#f39800;
  --blue:#2b8fd6;
  --text:#333;
  --muted:#666;
  --line:#ddd;
  --gray-bg:#f1f1f1;
  --footer-bg:#e9e9e9;
  --white:#fff;
  --diagram-blue:#dce8f3;
  --diagram-orange:#fbe3bd;
}
*{margin:0;padding:0;box-sizing:border-box}
html,body{width:1200px;height:4884px;overflow:hidden}
body{font-family:"Noto Sans JP",sans-serif;color:var(--text);background:var(--white);position:relative;font-size:15px;line-height:1.7}
a{text-decoration:none}
.brand{font-weight:700;color:var(--text);letter-spacing:.06em;display:flex;align-items:center;gap:10px}
.brand-mark{width:14px;height:14px;background:var(--orange);display:inline-block}

/* header */
.site-header{height:168px;position:relative}
.header-top{position:absolute;left:180px;top:36px;display:flex;align-items:center;gap:24px}
.header-top .brand{font-size:38px}
.tagline{font-size:12px;line-height:1.5;color:var(--muted)}
.header-contact{position:absolute;right:140px;top:28px;text-align:right}
.tel{font-size:26px;font-weight:700;color:var(--text);line-height:1.1}
.hours{font-size:11px;color:var(--muted)}
.btn-contact{display:inline-block;margin-top:6px;background:var(--orange);color:var(--white);font-size:13px;padding:3px 22px}
.global-nav{position:absolute;left:100px;right:100px;top:118px;display:flex;border-top:1px solid var(--line)}
.global-nav a{flex:1;text-align:center;font-size:15px;color:var(--text);padding:8px 0;border-left:1px solid var(--line)}
.global-nav a:last-child{border-right:1px solid var(--line)}

/* hero */
.hero{height:512px;position:relative;background:linear-gradient(180deg,#d9dde2 0%,#c3c9cf 35%,#8d9198 70%,#5d6167 100%)}
.hero-copy{position:absolute;left:0;right:0;top:200px;text-align:center;color:var(--white)}
.hero-copy h1{font-size:48px;font-weight:700;letter-spacing:.04em;text-shadow:0 2px 6px rgba(0,0,0,.35)}
.hero-copy .brand{color:var(--white);font-size:44px;justify-content:center;margin-top:14px}
.slider-dots{height:50px;display:flex;justify-content:center;align-items:center;gap:12px}
.slider-dots span{width:10px;height:10px;border-radius:50%;background:#ccc}
.slider-dots span.active{background:var(--orange)}

.intro{height:190px;text-align:center;font-size:17px;line-height:1.9;padding-top:20px}

/* features */
.features{height:600px;background:var(--orange);position:relative;color:var(--white)}
.feature-list{position:absolute;left:150px;right:150px;top:80px;display:flex;justify-content:space-between}
.feature{width:280px;text-align:center}
.feature-circle{width:230px;height:230px;border-radius:50%;background:var(--white);margin:0 auto;display:flex;flex-direction:column;align-items:center;justify-content:center;color:var(--text);font-size:16px;line-height:1.6;font-weight:500}
.feature-icon{width:58px;height:58px;border-radius:50%;background:var(--orange);margin-bottom:12px;display:flex;align-items:center;justify-content:center}
.feature p{font-size:13px;margin-top:18px;line-height:1.7;white-space:nowrap}
.btn-outline-white{position:absolute;left:460px;top:490px;width:280px;height:76px;border:2px solid var(--white);color:var(--white);display:flex;align-items:center;justify-content:center;font-size:18px}

/* compare */
.section-title{text-align:center;font-size:36px;font-weight:700;letter-spacing:.04em}
.compare{height:792px;position:relative}
.compare .section-title{position:absolute;top:72px;left:0;right:0}
.compare-col{position:absolute;top:180px;width:440px}
.compare-col.left{left:160px}
.compare-col.right{left:700px}
.compare-col h3{font-size:32px;font-weight:500;color:var(--muted);margin-bottom:20px;line-height:1.3}
.compare-col .brand{font-size:34px;margin-bottom:20px;line-height:1.3}
.diagram{width:300px;height:170px}
.diagram.estimate{background:linear-gradient(180deg,var(--diagram-blue),#c9d7e6)}
.diagram.direct{background:linear-gradient(180deg,var(--diagram-orange),#f6cf8f)}
.compare-col ul{list-style:none;font-size:13px;color:var(--muted);margin-top:40px;line-height:1.8}
.compare-col li{margin-bottom:10px}

/* faq */
.faq{height:808px;background:var(--gray-bg);position:relative}
.faq .section-title{position:absolute;top:58px;left:0;right:0;font-weight:500}
.faq-grid{position:absolute;left:110px;right:110px;top:160px;display:grid;grid-template-columns:repeat(3,1fr);column-gap:40px;row-gap:40px}
.faq-item{font-size:13px;line-height:1.7}
.faq-row{display:flex;gap:14px;align-items:flex-start}
.faq-q{padding-bottom:14px;border-bottom:1px solid var(--line);margin-bottom:14px}
.badge{flex:0 0 36px;height:36px;border-radius:50%;color:var(--white);font-weight:700;display:flex;align-items:center;justify-content:center;font-size:17px}
.badge.q{background:var(--blue)}
.badge.a{background:var(--orange)}

/* results */
.results{height:1280px;position:relative}
.results .section-title{position:absolute;top:80px;left:0;right:0;font-weight:500}
.result-card{position:absolute;left:180px;width:840px;height:400px;display:flex;gap:40px}
.result-card.first{top:180px}
.result-card.second{top:620px}
.result-photo{width:280px;height:400px;flex:0 0 280px}
.photo-tower{background:linear-gradient(180deg,#cfd6de 0%,#a9b1ba 50%,#7d848c 100%)}
.photo-room{background:linear-gradient(180deg,#e8e4dc 0%,#c9c1b3 55%,#8f8677 100%)}
.result-body{flex:1;padding-top:10px}
.result-body h3{font-size:24px;font-weight:700;margin-bottom:20px}
.result-inner{display:flex;gap:30px}
.spec{width:240px;border-collapse:collapse;font-size:14px}
.spec td{border-bottom:1px solid var(--line);padding:8px 6px}
.spec td:last-child{text-align:right}
.result-desc{flex:1;font-size:13px;color:var(--muted);line-height:1.7}
.btn-detail{display:block;margin-top:24px;margin-left:270px;width:250px;height:42px;background:var(--orange);color:var(--white);text-align:center;line-height:42px;font-size:15px}
.btn-more{position:absolute;left:455px;top:1072px;width:290px;height:68px;background:var(--orange);color:var(--white);display:flex;align-items:center;justify-content:center;font-size:17px}

.cta-row{position:absolute;left:0;right:0;top:4400px;display:flex;justify-content:center;gap:100px}
.cta{width:290px;height:60px;display:flex;align-items:center;justify-content:center;font-size:16px;border:2px solid}
.cta.assess{border-color:var(--blue);color:var(--blue)}
.cta.visit{border-color:var(--orange);color:var(--orange)}
.page-top{position:absolute;left:976px;top:4408px;width:44px;height:44px;border-radius:50%;background:var(--orange)}

/* footer */
.site-footer{position:absolute;left:0;right:0;top:4480px;height:372px;background:var(--footer-bg)}
.footer-brand{position:absolute;left:180px;top:44px;display:flex;gap:20px;align-items:center}
.footer-brand .brand{font-size:34px}
.footer-nav{position:absolute;left:660px;top:46px;display:flex;gap:40px;font-size:12px;color:var(--muted);line-height:2}
.footer-nav ul{list-style:none}
.footer-company{position:absolute;left:180px;top:140px;font-size:12px;color:var(--muted);line-height:1.8;width:360px}
.footer-company strong{color:var(--text);font-size:14px}
.footer-note{position:absolute;left:660px;top:160px;width:360px;font-size:12px;color:var(--muted);line-height:1.8}
.copyright{position:absolute;left:0;right:0;top:4852px;height:32px;background:var(--white);text-align:center;font-size:11px;color:var(--muted);line-height:32px}
</style>
</head>
<body>

<header class="site-header">
  <div class="header-top">
    <div class="brand"><span class="brand-mark"></span>タカミエ</div>
    <p class="tagline">7階以上の高層階限定<br>マンション買取サービス</p>
  </div>
  <div class="header-contact">
    <div class="tel">06-4821-3097</div>
    <div class="hours">受付時間 10:00〜19:00（水曜定休）</div>
    <span class="btn-contact">お問い合わせはこちら</span>
  </div>
  <nav class="global-nav">
    <a>タカミエとは</a><a>買取について</a><a>買取実績</a><a>買取物件査定</a><a>ご来店予約</a>
  </nav>
</header>

<section class="hero" role="img" aria-label="高層階から見下ろした都市の街並みの写真">
  <div class="hero-copy">
    <h1>7階以上のお部屋、買い取ります。</h1>
    <div class="brand">タカミエ</div>
  </div>
</section>
<div class="slider-dots"><span class="active"></span><span></span><span></span></div>

<section class="intro">
  <p>「タカミエ」は、7階以上の高層階のマンション売買サービスです。<br>
  見晴らしのよい高層階のマンションは、それだけで心を癒してくれる特別な価値を持っています。<br>
  「タカミエ」は、その価値に見合った金額で、マンションを買い取らせていただきます。</p>
</section>

<section class="features">
  <div class="feature-list">
    <div class="feature">
      <div class="feature-circle">
        <div class="feature-icon"><svg width="30" height="30" viewBox="0 0 30 30"><rect x="4" y="6" width="18" height="18" fill="none" stroke="#fff" stroke-width="2.5"/><path d="M12 18 L24 6 L27 9 L15 21 L11 22 Z" fill="#fff"/></svg></div>
        納得の金額を<br>ご提示します！
      </div>
      <p>高層マンションに特化したノウハウで、<br>眺望や階数の価値を正しく評価し、<br>納得の買取価格をご提示します。</p>
    </div>
    <div class="feature">
      <div class="feature-circle">
        <div class="feature-icon"><svg width="30" height="30" viewBox="0 0 30 30"><rect x="7" y="7" width="16" height="16" rx="2" fill="#fff"/></svg></div>
        売買もスムーズ！<br>素早く現金化<br>できます。
      </div>
      <p>自社買取なので買い手探しが不要、<br>スムーズに売却が進みます。<br>最短数日での現金化も可能です。</p>
    </div>
    <div class="feature">
      <div class="feature-circle">
        <div class="feature-icon"><svg width="30" height="30" viewBox="0 0 30 30"><path d="M7 15 L13 21 L24 9" fill="none" stroke="#fff" stroke-width="3.5" stroke-linecap="round" stroke-linejoin="round"/></svg></div>
        査定は無料！<br>仲介手数料も<br>かかりません。
      </div>
      <p>もちろん査定は無料です。<br>当社が直接買取するので、<br>仲介手数料もかかりません。</p>
    </div>
  </div>
  <a class="btn-outline-white">詳しくはこちら</a>
</section>

<section class="compare">
  <h2 class="section-title">一括見積もりサイトとの違い</h2>
  <div class="compare-col left">
    <h3>一括見積もりサイト</h3>
    <div class="diagram estimate" role="img" aria-label="一括見積もりサイトから複数の不動産業者を経てお客様につながる流れの図"></div>
    <ul>
      <li>・買い取り業者が多く、たらい回しにされてしまう、電話やメールが何度も来るなど、面倒な手間がかかります。</li>
      <li>・業者ごとに査定基準が異なるため、金額が大きくばらつき、比較に時間がかかります。</li>
    </ul>
  </div>
  <div class="compare-col right">
    <div class="brand"><span class="brand-mark"></span>タカミエ</div>
    <div class="diagram direct" role="img" aria-label="当社が直接お客様から買い取る流れの図"></div>
    <ul>
      <li>・高層階の物件に特化した専門チームが査定を担当し、眺望の価値まで正しく評価します。</li>
      <li>・窓口は当社ひとつだけなので、やり取りもシンプル。余計な連絡は一切ありません。</li>
      <li>・当社が直接買い取るため、仲介手数料も不要で安心です。</li>
    </ul>
  </div>
</section>

<section class="faq">
  <h2 class="section-title">よくある質問</h2>
  <div class="faq-grid">
    <div class="faq-item"><div class="faq-row faq-q"><span class="badge q">Q</span><p>質問の文言が入ります。質問の文言が入ります。</p></div><div class="faq-row"><span class="badge a">A</span><p>回答の文言が入ります。回答の文言が入ります。回答の文言が入ります。回答の文言が入ります。回答の文言が入ります。</p></div></div>
    <div class="faq-item"><div class="faq-row faq-q"><span class="badge q">Q</span><p>質問の文言が入ります。質問の文言が入ります。</p></div><div class="faq-row"><span class="badge a">A</span><p>回答の文言が入ります。回答の文言が入ります。回答の文言が入ります。回答の文言が入ります。回答の文言が入ります。</p></div></div>
    <div class="faq-item"><div class="faq-row faq-q"><span class="badge q">Q</span><p>質問の文言が入ります。質問の文言が入ります。</p></div><div class="faq-row"><span class="badge a">A</span><p>回答の文言が入ります。回答の文言が入ります。回答の文言が入ります。回答の文言が入ります。回答の文言が入ります。</p></div></div>
    <div class="faq-item"><div class="faq-row faq-q"><span class="badge q">Q</span><p>質問の文言が入ります。質問の文言が入ります。</p></div><div class="faq-row"><span class="badge a">A</span><p>回答の文言が入ります。回答の文言が入ります。回答の文言が入ります。回答の文言が入ります。回答の文言が入ります。</p></div></div>
    <div class="faq-item"><div class="faq-row faq-q"><span class="badge q">Q</span><p>質問の文言が入ります。質問の文言が入ります。</p></div><div class="faq-row"><span class="badge a">A</span><p>回答の文言が入ります。回答の文言が入ります。回答の文言が入ります。回答の文言が入ります。回答の文言が入ります。</p></div></div>
    <div class="faq-item"><div class="faq-row faq-q"><span class="badge q">Q</span><p>質問の文言が入ります。質問の文言が入ります。</p></div><div class="faq-row"><span class="badge a">A</span><p>回答の文言が入ります。回答の文言が入ります。回答の文言が入ります。回答の文言が入ります。回答の文言が入ります。</p></div></div>
  </div>
</section>

<section class="results">
  <h2 class="section-title">買取実績</h2>
  <article class="result-card first">
    <div class="result-photo photo-tower" role="img" aria-label="高層マンションの外観写真"></div>
    <div class="result-body">
      <h3>物件名が入ります。物件名が入ります。</h3>
      <div class="result-inner">
        <table class="spec"><tr><td>階</td><td>18階</td></tr><tr><td>間取り</td><td>2LDK</td></tr><tr><td>価格</td><td>3000万円</td></tr><tr><td>地域</td><td>大阪市内</td></tr></table>
        <p class="result-desc">物件の詳細文言が入ります。物件の詳細文言が入ります。物件の詳細文言が入ります。物件の詳細文言が入ります。物件の詳細文言が入ります。</p>
      </div>
      <a class="btn-detail">詳細を見る</a>
    </div>
  </article>
  <article class="result-card second">
    <div class="result-photo photo-room" role="img" aria-label="眺望のよい室内の写真"></div>
    <div class="result-body">
      <h3>物件名が入ります。物件名が入ります。</h3>
      <div class="result-inner">
        <table class="spec"><tr><td>階</td><td>18階</td></tr><tr><td>間取り</td><td>2LDK</td></tr><tr><td>価格</td><td>3000万円</td></tr><tr><td>地域</td><td>大阪市内</td></tr></table>
        <p class="result-desc">物件の詳細文言が入ります。物件の詳細文言が入ります。物件の詳細文言が入ります。物件の詳細文言が入ります。物件の詳細文言が入ります。</p>
      </div>
      <a class="btn-detail">詳細を見る</a>
    </div>
  </article>
  <a class="btn-more">買取実績をもっと見る</a>
</section>

<div class="cta-row">
  <a class="cta assess">買取物件査定はこちら</a>
  <a class="cta visit">ご来店予約はこちら</a>
</div>
<a class="page-top" aria-label="ページトップへ"><svg width="44" height="44" viewBox="0 0 44 44"><path d="M14 25 L22 17 L30 25" fill="none" stroke="#fff" stroke-width="3" stroke-linecap="round" stroke-linejoin="round"/></svg></a>

<footer class="site-footer">
  <div class="footer-brand">
    <div class="brand"><span class="brand-mark"></span>タカミエ</div>
    <p class="tagline">7階以上の高層階限定<br>マンション買取サービス</p>
  </div>
  <div class="footer-nav">
    <ul><li>・タカミエとは</li><li>・よくある質問</li></ul>
    <ul><li>・買取について</li><li>・お問い合わせ</li></ul>
    <ul><li>・買取実績</li><li>・プライバシーポリシー</li></ul>
    <ul><li>・ご来店予約</li><li>・運営会社</li></ul>
  </div>
  <div class="footer-company">
    <strong>運営：株式会社タカミエコミュニティ</strong><br>
    〒530-0000<br>
    大阪府大阪市北区中央1丁目2番3号<br>
    サンプルビル7階<br>
    TEL 06-4821-3097
  </div>
  <p class="footer-note">「タカミエ」は、不動産買取会社・株式会社タカミエコミュニティが運営する高層階マンション専門の買取サービスです。お気軽にご相談ください。</p>
</footer>
<div class="copyright">Copyright © 2017 Kestrel Habitat Co.,Ltd All Rights Reserved.</div>

</body>
</html>
```